Bright Oak Fitness Facility Business Cards

Business Card Design that incorporates the logo and tagline

Target Market(s)

Fitness, People Who Exercise

Contact Information for Business Card

2718 Harrow Creek Bend
Cedar Vale, Ohio 44990
Phone: 352-555-Team (8326)
www.brightoakfitness.example
info@brightoakfitness.example

Requirements
Must have
• Logo, Address, Website, email and tagline "Stronger Every Day". Colors should be red/black/grey/white

```html
<!DOCTYPE html>
<html lang="en">
<head>
<meta charset="utf-8">
<title>Bright Oak Fitness – Business Card</title>
<link rel="stylesheet" href="https://fonts.googleapis.com/css2?family=Montserrat:wght@400;500;600&family=Oswald:wght@500&display=swap">
<style>
  :root {
    --bg: #e7e4df;
    --card: #ffffff;
    --ink: #2f3034;
    --grey: #6d6e72;
    --red: #e5404f;
    --band: #151515;
    --rule: #8a8b8e;
  }
  * { margin: 0; padding: 0; box-sizing: border-box; }
  html, body { width: 1200px; height: 1023px; overflow: hidden; }
  body {
    background: var(--bg);
    font-family: "Montserrat", sans-serif;
    color: var(--ink);
    display: flex; align-items: center; justify-content: center;
  }
  .card {
    position: relative;
    width: 900px; height: 514px;
    background: var(--card);
    border-radius: 22px;
    overflow: hidden;
    box-shadow: 0 10px 30px rgba(0,0,0,.18);
  }
  .brand { position: absolute; left: 78px; top: 92px; }
  .brand-name {
    display: flex; align-items: center; gap: 16px;
    font-size: 46px; font-weight: 600; letter-spacing: 1px;
    color: var(--ink); text-transform: uppercase; white-space: nowrap;
  }
  .brand-mark { width: 22px; height: 22px; background: var(--red); flex: none; }
  .brand-tagline {
    margin-top: 12px; padding-top: 10px;
    border-top: 2px solid var(--ink);
    width: 360px;
    font-size: 15px; font-weight: 500; letter-spacing: 7px;
    color: var(--red); text-transform: uppercase; white-space: nowrap;
  }
  .person { position: absolute; left: 78px; top: 262px; }
  .person-name {
    font-family: "Oswald", sans-serif; font-weight: 500;
    font-size: 48px; line-height: 1; color: var(--red);
    text-transform: uppercase; letter-spacing: .5px; white-space: nowrap;
  }
  .person-role { margin-top: 8px; font-size: 18px; color: var(--ink); text-align: right; }
  .divider {
    position: absolute; left: 452px; top: 262px;
    width: 1.5px; height: 96px; background: var(--rule);
  }
  .contacts { position: absolute; left: 486px; top: 256px; list-style: none; }
  .contacts li {
    display: flex; align-items: center; gap: 12px;
    font-size: 18px; line-height: 36px; color: var(--ink); white-space: nowrap;
  }
  .contacts svg { width: 13px; height: 13px; fill: var(--red); flex: none; }
  .contacts .accent { color: var(--red); }
  .band-rule { position: absolute; left: 0; right: 0; top: 420px; height: 5px; background: var(--red); }
  .band {
    position: absolute; left: 0; right: 0; top: 425px; bottom: 0;
    background: var(--band);
    display: flex; align-items: center; padding-left: 78px;
    color: #fff; font-size: 20px; letter-spacing: .3px; white-space: nowrap;
  }
</style>
</head>
<body>
  <article class="card">
    <header class="brand">
      <div class="brand-name"><span class="brand-mark"></span>Bright Oak Fitness</div>
      <div class="brand-tagline">Stronger every day</div>
    </header>

    <section class="person">
      <div class="person-name">Dana Whitfield</div>
      <div class="person-role">Director</div>
    </section>

    <div class="divider"></div>

    <ul class="contacts">
      <li>
        <svg viewBox="0 0 24 24"><path d="M6.6 10.8a15.2 15.2 0 0 0 6.6 6.6l2.2-2.2a1 1 0 0 1 1-.25 11.4 11.4 0 0 0 3.6.57 1 1 0 0 1 1 1V20a1 1 0 0 1-1 1A17 17 0 0 1 3 4a1 1 0 0 1 1-1h3.5a1 1 0 0 1 1 1c0 1.25.2 2.45.57 3.57a1 1 0 0 1-.25 1z"/></svg>
        555-010-(8326)
      </li>
      <li>
        <svg viewBox="0 0 24 24"><path d="M2 5h20v14H2zm2 2v.5l8 5 8-5V7zm0 2.8V17h16V9.8l-8 5z"/></svg>
        info@brightoakfitness.example
      </li>
      <li>
        <svg viewBox="0 0 24 24"><path d="M12 2a10 10 0 1 0 0 20 10 10 0 0 0 0-20zm6.9 9h-3a15 15 0 0 0-1.3-5.6A8 8 0 0 1 18.9 11zM12 4.1c.9 1.2 1.8 3.6 1.9 6.9h-3.8c.1-3.3 1-5.7 1.9-6.9zM9.4 5.4A15 15 0 0 0 8.1 11h-3a8 8 0 0 1 4.3-5.6zM5.1 13h3a15 15 0 0 0 1.3 5.6A8 8 0 0 1 5.1 13zm6.9 6.9c-.9-1.2-1.8-3.6-1.9-6.9h3.8c-.1 3.3-1 5.7-1.9 6.9zm2.6-1.3a15 15 0 0 0 1.3-5.6h3a8 8 0 0 1-4.3 5.6z"/></svg>
        <span>www.<span class="accent">brightoakfitness</span>.example</span>
      </li>
    </ul>

    <div class="band-rule"></div>
    <footer class="band">2718 Harrow Creek Bend Cedar Vale, Ohio 44990</footer>
  </article>
</body>
</html>
```